Real Estate Office Front Facade Redesign - ideas needed

Kindly read this brief thoroughly as there are 2 deliverables:
1. Office building façade redesign (see attached logo and also photo of our office building façade)
2. I also require a design for a freestanding signboard that will be coordinated with the design of the office front please see the images attached labelled signboard.

Deliverable number 1:
I am looking for a minimalist contemporary design with strong colours to draw the attention of the passing Traffic.

The office facade is to be repainted so you may choose to recolour the office in any way to coordinate with logo however the attached logo must remain as is. I prefer the colours red black and white or shades of these colours.

Vireo property managers is a new company looking to target property investors in the local area. Most of our clients are from a middle to upper income demographic. We help these investors to rent out their properties and ensure they are maintained in good condition and provide a regular income.

The area we operate in is centrally located and close to the central business district of Perth.

Our office is situated in a residential area on a busy road facing diagonally at 45° down the road. People see our office from their cars whilst driving to work, there is no pedestrian traffic in the area. Therefore the office façade needs to stand out and any signage must be read by quickly passing traffic or convey our brand in seconds. Whilst the view of the office from the road is obscured somewhat by trees from a distance, once within 50 to 100 m of the office the full face of the office front is visible facing directly at the driver.

No measurements are provided for the façade of the office (please see the photo provided), this is a blank canvas as the whole building will be repainted to fit in with YOUR design. A logo is also attached. The colours red black and white are preferred.

Please provide an image of the office with signage/colours superimposed.

Deliverable number 2:
Also attached is an image of a freestanding sign for which I require a design. This sign is used for advertising properties for lease or sale which will be erected outside the front of residential houses. Again this sign needs to be bold and bright with a contemporary design. It needs to stand out from the crowd of many other signs in the area, whilst the sign advertises the property it must also promote our company brand by having a prominent logo. The size of these signboards will either be 1250 mm x 900 mm or 1800 mm x 625 mm. Please note that this sign must be rectangular in shape and cannot have any text or logo protruding outside of the lines of the rectangular sign due to cost restrictions.

Target Market(s)

Industry/Entity Type

Real Estate

Font styles to use
Sans Serif

Colors
ec1f27
ffffff
000000

Requirements
Must have
• Contemporary uncluttered design using the colours red black and white of shades of.
Nice to have
• A prominent logo with the words "Property Managers" easily read by passing traffic.
• Files provided with editable text and the name of the font used.
Should not have
• designs protruding outside of the overall building facia or sign rectangle.

```html
<!DOCTYPE html>
<html lang="en">
<head>
<meta charset="utf-8">
<title>Vireo Property Managers – Signage and Office Front</title>
<link rel="stylesheet" href="https://fonts.googleapis.com/css2?family=Montserrat:wght@300;400;500;700;800&display=swap">
<style>
  :root{
    --red:#ec1f27;
    --white:#ffffff;
    --ink:#2b2b2d;
    --panel:#252f37;
    --label:#b9c0c6;
    --footer:#46525c;
    --wall:#2c2c2e;
    --frame:#f4f4f4;
    --glass:#3a4044;
    --muted:#6b7176;
  }
  *{margin:0;padding:0;box-sizing:border-box}
  html,body{width:1200px;height:542px;overflow:hidden;background:var(--white);font-family:"Montserrat",Arial,sans-serif}
  .board{position:relative;width:1200px;height:542px;overflow:hidden}
  .abs{position:absolute}

  /* Left panel: free standing sign */
  .sign-panel{left:0;top:0;width:265px;height:542px;background:var(--panel)}
  .panel-label{left:0;width:265px;top:24px;line-height:14px;text-align:center;font-size:11px;letter-spacing:1px;color:var(--label);font-weight:400}
  .sign{left:54px;top:56px;width:156px;height:448px;background:var(--white);border-radius:8px 8px 0 0;overflow:visible}
  .sign-brand{left:0;width:156px;text-align:center;white-space:nowrap}
  .brand-mark{left:53px;top:42px;width:50px;height:50px;background:var(--red);border-radius:5px}
  .brand-name{top:142px;font-size:25px;line-height:25px;font-weight:300;letter-spacing:3px;color:var(--ink);padding-left:3px}
  .brand-sub{top:172px;font-size:7px;line-height:8px;letter-spacing:.8px;color:var(--red);font-weight:400}
  .lease-band{left:0;top:196px;width:156px;height:94px;background:var(--red);color:var(--white);text-align:center;font-weight:800;font-size:37px;line-height:36px;padding-top:11px;letter-spacing:-.5px}
  .lease-notch{left:72px;top:289px;width:0;height:0;border-left:6px solid transparent;border-right:6px solid transparent;border-top:6px solid var(--red)}
  .contact{left:0;width:156px;text-align:center;line-height:20px;white-space:nowrap}
  .contact-label{font-size:17px;font-weight:700;color:var(--red)}
  .contact-number{font-size:18px;font-weight:400;color:var(--ink);letter-spacing:.5px}
  .sign-footer{left:0;top:422px;width:156px;height:26px;background:var(--footer);color:var(--white);font-size:8.5px;text-align:center;line-height:26px;letter-spacing:.3px;white-space:nowrap}
  .sign-leg{top:504px;width:8px;height:14px;background:#111}

  /* Right: office front */
  .street{left:265px;top:0;width:935px;height:542px}
  .office-label{left:265px;width:982px;top:135px;line-height:14px;text-align:center;font-size:11px;letter-spacing:1px;color:var(--muted)}
  .fascia{left:294px;top:164px;width:871px;height:50px;background:var(--white)}
  .fascia-band{left:60px;top:0;width:751px;height:50px;background:var(--wall);color:var(--white);font-weight:300;font-size:33px;letter-spacing:8.5px;text-align:center;line-height:50px;white-space:nowrap;padding-left:8px}
  .fascia-mark{top:13px;width:24px;height:24px;background:var(--red);border-radius:3px}
  .soffit{left:294px;top:214px;width:871px;height:24px;background:#e9eaea}
  .wall{left:342px;top:238px;width:782px;height:206px;background:var(--wall)}
  .wall-block{top:20px;height:174px;background:var(--red);border-radius:12px}
  .window{background:var(--frame);box-shadow:0 1px 2px rgba(0,0,0,.3)}
  .window-pane{position:absolute;left:7px;top:7px;right:7px;bottom:16px;background:var(--glass)}
  .window-url{position:absolute;left:0;right:0;bottom:3px;line-height:8px;text-align:center;font-size:6px;color:var(--ink);font-weight:500;white-space:nowrap}
  .door-sign{left:790px;top:262px;width:130px;text-align:center;color:var(--white);white-space:nowrap}
  .door-name{font-size:18px;line-height:20px;font-weight:300;letter-spacing:2px}
  .door-sub{font-size:6.5px;line-height:8px;letter-spacing:1px;margin-top:3px}
  .door-leaf{top:312px;width:51px;height:121px;border:1px solid #8a8f93;background:rgba(255,255,255,.05)}
  .door-mark{position:absolute;left:16px;top:50px;width:18px;height:18px;background:var(--red);border-radius:2px}
</style>
</head>
<body>
<main class="board">

  <section class="abs sign-panel" aria-label="Free standing sign">
    <p class="abs panel-label">Free Standing Signage</p>
    <div class="abs sign">
      <div class="abs brand-mark"></div>
      <p class="abs sign-brand brand-name">VIREO</p>
      <p class="abs sign-brand brand-sub">PROPERTY MANAGERS</p>
      <div class="abs lease-band">FOR<br>LEASE</div>
      <div class="abs lease-notch"></div>
      <p class="abs contact contact-label" style="top:312px">MOBILE</p>
      <p class="abs contact contact-number" style="top:334px">0400 123 456</p>
      <p class="abs contact contact-label" style="top:363px">OFFICE</p>
      <p class="abs contact contact-number" style="top:384px">9300 1234</p>
      <div class="abs sign-footer">www.vireoproperty.com.au</div>
    </div>
    <div class="abs sign-leg" style="left:70px"></div>
    <div class="abs sign-leg" style="left:186px"></div>
  </section>

  <svg class="abs street" width="935" height="542" role="img" aria-label="Photograph of the office street front with sky and pavement">
    <defs>
      <linearGradient id="streetTone" x1="0" y1="0" x2="0" y2="1">
        <stop offset="0" stop-color="#dfe8ee"/>
        <stop offset="0.45" stop-color="#f3f5f6"/>
        <stop offset="0.82" stop-color="#d9d7d3"/>
        <stop offset="1" stop-color="#c9c6c1"/>
      </linearGradient>
    </defs>
    <rect width="935" height="542" fill="url(#streetTone)"/>
  </svg>

  <p class="abs office-label">Office Recolor</p>

  <section class="abs fascia" aria-label="Fascia sign">
    <div class="abs fascia-mark" style="left:24px"></div>
    <div class="abs fascia-band">VIREO PROPERTY MANAGERS</div>
    <div class="abs fascia-mark" style="left:823px"></div>
  </section>
  <div class="abs soffit"></div>

  <section class="abs wall" aria-label="Office front wall">
    <div class="abs wall-block" style="left:0;width:86px"></div>
    <div class="abs wall-block" style="left:228px;width:120px"></div>
    <div class="abs wall-block" style="left:688px;width:94px"></div>
  </section>

  <div class="abs window" style="left:382px;top:300px;width:210px;height:102px;transform:rotate(-1deg)">
    <div class="window-pane"></div><p class="window-url">www.vireoproperty.com.au</p>
  </div>
  <div class="abs window" style="left:661px;top:306px;width:127px;height:92px;transform:rotate(.6deg)">
    <div class="window-pane"></div><p class="window-url">www.vireoproperty.com.au</p>
  </div>
  <div class="abs window" style="left:922px;top:306px;width:139px;height:92px;transform:rotate(-.6deg)">
    <div class="window-pane"></div><p class="window-url">www.vireoproperty.com.au</p>
  </div>

  <div class="abs door-sign">
    <p class="door-name">VIREO</p>
    <p class="door-sub">PROPERTY MANAGERS</p>
  </div>
  <div class="abs door-leaf" style="left:800px"><div class="door-mark"></div></div>
  <div class="abs door-leaf" style="left:859px"><div class="door-mark"></div></div>

</main>
</body>
</html>
```